clean web design for a recruitment company

We need a web design for a company called 'TORAVI' recruitment. We are a new age recruitment companies that selects people by their true nature, values and what they can bring to the table as a tangible talent. We are all here possessing a certain talent, whatever that could be that the world needs. The final design should communicate professionalism and strongly embedded etiquette we believe in and a branding promise 'Seeing ones true nature'. Our companies values are integrity, giving away to the community, cherishing the sharing of our talent, time and helping one another.

Target Market(s)

Gulf Countries

Industry/Entity Type

It Company

Number of Pages Required

1 page

Font styles to use
Serif

Requirements
Must have
• Clear and readable font, user friendly structure and easy navigation menus.
Nice to have
• Extra sort of ideas on images we may use, tag lines etc. sample sites we love site:https://www.velmaroque.com/
• http://www.dorisaklund.com/
• http://www.pebblemoorhouse.com/idea-gallery/
Should not have
• all sort of colors, big combination of fonts, images with people in the office or people in suits likewise all the typical industry web sites

```html
<!DOCTYPE html>
<html lang="en">
<head>
<meta charset="utf-8">
<title>Toravi Recruitment</title>
<link href="https://fonts.googleapis.com/css2?family=Lato:wght@300;400;700;900&display=swap" rel="stylesheet">
<style>
:root{
  --ink:#2b2b2b;
  --text:#6f6f6f;
  --muted:#9a9a9a;
  --line:#d8d8d8;
  --soft:#f3f3f3;
  --white:#ffffff;
  --dark:#2f2f2f;
  --footer:#262626;
}
*{box-sizing:border-box;margin:0;padding:0}
html,body{width:1200px;height:2727px;overflow:hidden;background:var(--white)}
body{font-family:"Lato",sans-serif;color:var(--text);position:relative}
.abs{position:absolute}
.center{left:0;width:1200px;text-align:center}

/* header */
.brand-mark{left:584px;top:30px;width:32px;height:60px;background:var(--ink)}
.brand-name{top:100px;font-size:44px;font-weight:700;color:var(--ink);letter-spacing:1px;line-height:44px}
.brand-sub{top:146px;font-size:14px;letter-spacing:5px;color:var(--ink)}

/* nav */
.nav{top:190px;left:0;width:1200px;height:42px;border-top:2px solid var(--ink);border-bottom:1px solid var(--line)}
.nav a{position:absolute;top:0;height:40px;line-height:40px;font-size:12px;color:var(--text);text-decoration:none}
.nav a.active{background:#555;color:var(--white);width:91px;text-align:center}

/* hero */
.hero{top:232px;left:0;width:1200px;height:532px;background:linear-gradient(180deg,#6d6d6d 0%,#a9a9a9 45%,#3c3c3c 78%,#1d1d1d 100%)}
.hero-title{top:468px;font-size:33px;font-weight:900;color:var(--white);letter-spacing:1px}
.hero-arrow{top:470px;width:26px;height:26px;background:rgba(255,255,255,.25)}
.dots{top:704px;left:0;width:1200px;display:flex;justify-content:center;gap:6px}
.dots span{width:7px;height:7px;border-radius:50%;background:var(--white);opacity:.6}
.dots span:first-child{opacity:1}

/* quote */
.quote{top:764px;left:0;width:1200px;height:313px;background:var(--soft)}
.quote-mark{top:826px;font-size:60px;color:#aaa;font-weight:300;line-height:60px}
.quote-text{top:888px;left:164px;width:872px;text-align:center;font-size:14.5px;line-height:26px;color:var(--text)}
.rule{height:2px;background:#bdbdbd;width:44px}

/* intro */
.intro-title{top:1170px;font-size:28px;font-weight:300;color:#555;line-height:34px;letter-spacing:1px}
.intro-text{left:300px;width:600px;text-align:center;font-size:11px;line-height:17px;color:var(--muted)}
.btn{border:1px solid var(--line);font-size:11px;letter-spacing:1px;color:var(--muted);text-align:center;line-height:36px;height:38px}

/* services */
.service{top:1519px;width:400px;height:235px}
.service-title{top:90px;left:0;width:400px;text-align:center;font-size:22px;font-weight:300;color:var(--white);letter-spacing:1px}
.service-sub{top:128px;left:0;width:400px;text-align:center;font-size:10px;color:var(--white);opacity:.85}

/* team */
.team-title{top:1826px;font-size:22px;font-weight:300;color:#555;letter-spacing:1px}
.card{top:1942px;width:237px;height:218px;background:#e7e7e7}
.card-bar{position:absolute;left:0;bottom:0;width:237px;height:52px;background:var(--dark);color:var(--white);font-size:11px;font-weight:700;padding:18px 0 0 18px}
.card-bar .stars{color:#888;font-weight:400;margin-left:10px;letter-spacing:1px}
.card-open{position:absolute;left:0;top:95px;width:237px;height:123px;background:var(--dark);color:var(--white);padding:12px 16px;font-size:10px;line-height:14px}
.card-open b{display:inline-block;font-size:11px;margin-bottom:6px}
.card-open .more{display:block;margin-top:10px;font-size:9px;color:#ccc}

/* clients */
.clients{top:2332px;left:0;width:1200px;height:90px;border-top:1px solid var(--line)}
.client{position:absolute;top:30px;font-size:22px;font-weight:700;color:#8a8a8a}

/* footer */
.footer{top:2422px;left:0;width:1200px;height:264px;background:linear-gradient(180deg,#333 0%,var(--footer) 100%)}
.social{top:2480px;left:0;width:1200px;display:flex;justify-content:center;gap:10px}
.social span{width:20px;height:20px;background:#e0e0e0}
.footer-title{top:2518px;font-size:20px;font-weight:300;color:var(--white);letter-spacing:1px}
.footer-text{font-size:11px;color:#bbb;line-height:16px}
.copy{top:2700px;font-size:10px;color:var(--muted)}
</style>
</head>
<body>

<header>
  <div class="abs brand-mark"></div>
  <div class="abs center brand-name">toravi</div>
  <div class="abs center brand-sub">RECRUITMENT</div>
</header>

<nav class="abs nav">
  <a class="active" style="left:264px">home</a>
  <a style="left:387px">team</a>
  <a style="left:460px">methedology</a>
  <a style="left:575px">specialist area</a>
  <a style="left:694px">clients</a>
  <a style="left:775px">candidates</a>
  <a style="left:876px">toravi group</a>
</nav>

<section>
  <div class="abs hero" role="img" aria-label="Black and white photo of a climber reaching the top of a rock at sunrise"></div>
  <h1 class="abs center hero-title">SEE THROUGH ONE TRUE NATURE</h1>
  <div class="abs hero-arrow" style="left:163px"><svg width="26" height="26"><path d="M15 8l-5 5 5 5" stroke="#fff" stroke-width="2" fill="none"/></svg></div>
  <div class="abs hero-arrow" style="left:1060px"><svg width="26" height="26"><path d="M11 8l5 5-5 5" stroke="#fff" stroke-width="2" fill="none"/></svg></div>
  <div class="abs dots"><span></span><span></span><span></span></div>
</section>

<section>
  <div class="abs quote"></div>
  <div class="abs center quote-mark">&ldquo;</div>
  <p class="abs quote-text">Inspired by the purpose in life and seeing through one true human nature. Let by community of enthusiastic recruiters and life experts that have the desire to share their passion and help you become the best version of who you may be in this life. Driven by belief that all of have that special talent that the world needs!</p>
  <div class="abs rule" style="left:578px;top:998px"></div>
</section>

<section>
  <h2 class="abs center intro-title">TRANSFORMED<br>THE IDEA OF RECRUITMENT SERVICES</h2>
  <div class="abs rule" style="left:578px;top:1254px"></div>
  <p class="abs intro-text" style="top:1276px">We look past the résumé to the person behind it, matching real talent with teams that value integrity, sharing and growth. Each placement begins with an honest talk about values.</p>
  <p class="abs intro-text" style="top:1322px">Our consultants listen first, then guide both sides toward a lasting fit built on trust and respect.</p>
  <div class="abs btn" style="left:567px;top:1404px;width:117px">READ MORE</div>
</section>

<section>
  <div class="abs service" style="left:0;background:linear-gradient(180deg,#7c7c7c,#3a3a3a)" role="img" aria-label="Muted photo of a meeting table">
    <div class="abs service-title">METHEDOLOGY</div>
    <div class="abs service-sub">HOW WE FIND THE RIGHT PEOPLE</div>
  </div>
  <div class="abs service" style="left:400px;background:linear-gradient(180deg,#8a8a8a,#444)" role="img" aria-label="Muted photo of a handshake">
    <div class="abs service-title">RECRUITEMENT SERVICES</div>
    <div class="abs service-sub">WHAT WE OFFER TO EMPLOYERS</div>
  </div>
  <div class="abs service" style="left:800px;background:linear-gradient(180deg,#9a9a9a,#4a4a4a)" role="img" aria-label="Muted photo of a workspace">
    <div class="abs service-title">SPECIALIST AREA</div>
    <div class="abs service-sub">FIELDS WHERE WE EXCEL TODAY</div>
  </div>
</section>

<section>
  <h2 class="abs center team-title">OUR TEAM</h2>
  <div class="abs rule" style="left:578px;top:1866px"></div>
  <p class="abs intro-text" style="top:1884px">Meet the people who guide every search, each one chosen for their care, insight and honest approach to talent.</p>

  <div class="abs card" style="left:235px">
    <div style="position:absolute;inset:0 0 123px 0;background:#dcdcdc" role="img" aria-label="Portrait of team member Amir T."></div>
    <div class="card-open"><b>AMIR T. <span style="color:#888;font-weight:400;margin-left:8px">★★★★★</span></b><br>We found the team to be very reasonable, efficient and professional. Our new hires fit right in.<span class="more">MORE</span></div>
  </div>
  <div class="abs card" style="left:505px" role="img" aria-label="Portrait of team member Sami K">
    <div class="card-bar">SAMI K<span class="stars">★★★★★</span></div>
  </div>
  <div class="abs card" style="left:777px" role="img" aria-label="Portrait of team member Lina R">
    <div class="card-bar">LINA R<span class="stars">★★★★★</span></div>
  </div>

  <div class="abs btn" style="left:556px;top:2203px;width:137px">VIEW ALL REVIEW</div>
</section>

<section class="abs clients">
  <span class="client" style="left:160px">Corvane</span>
  <span class="client" style="left:300px;font-size:16px;top:34px">Halden Institute</span>
  <span class="client" style="left:480px">Bravell</span>
  <span class="client" style="left:632px">Noxter</span>
  <span class="client" style="left:775px">Quarlo</span>
  <span class="client" style="left:920px">Veltris</span>
</section>

<footer>
  <div class="abs footer" role="img" aria-label="Dark collage of magazine pages in the background"></div>
  <div class="abs social"><span></span><span></span><span></span><span></span></div>
  <h2 class="abs center footer-title">FIND OUT MORE ABOUT WHATTORAVI</h2>
  <p class="abs center footer-text" style="top:2566px">Talent placed with care across the Gulf region, built on integrity,<br>sharing and giving back to the community we serve.</p>
  <p class="abs center footer-text" style="top:2612px">Palm Street, Harbor City, County 40211. Call: 0400 5512 7734</p>
  <p class="abs center copy">Copyright © 2015 toravi recruitment | privacy policy</p>
</footer>

</body>
</html>
```